Ironvale Holdings Business card

We need a an amazing matte black and gold card! W are a finance investing company so we want something that's eye catching and sleek. We want it to be attractive and sleek and represent money. Heck with would like the letters and lgo to be printed as 24k gold one day. We have the logo added so please use the color scheme with the logo and have that beautifully placed on one side.

Target Market(s)

Investors of all ages

Industry/Entity Type

Financial

Contact Information for Business Card

Black and matte with gold lettering follow logo colrs please.

Font styles to use
Other font styles liked:
• you decide

Colors

Designer to choose colors to be used in the design.

Requirements
Must have
• Matte Black and Gold, logo on one side. job title and name , website, phone number and email address on the other side
Nice to have
• Matte black and crisp finish to attract investors
Should not have
• playful, very professional!

```html
<!DOCTYPE html>
<html lang="en">
<head>
<meta charset="utf-8">
<title>Ironvale Holdings Business Card</title>
<link rel="stylesheet" href="https://fonts.googleapis.com/css2?family=Open+Sans:wght@400;600;700&display=swap">
<style>
  :root {
    --backdrop: #5a5a5a;
    --card-black: #2a2a2c;
    --card-black-deep: #222224;
    --emboss-tone: #38383a;
    --gold: #d9b42a;
    --ink-white: #f2f2f2;
  }
  * { margin: 0; padding: 0; box-sizing: border-box; }
  html, body {
    width: 1200px;
    height: 1125px;
    overflow: hidden;
    background: var(--backdrop);
    font-family: "Open Sans", Arial, sans-serif;
  }
  .stage {
    width: 1200px;
    height: 1125px;
    display: flex;
    flex-direction: column;
    align-items: center;
    justify-content: center;
    gap: 44px;
  }
  .card {
    position: relative;
    width: 860px;
    height: 492px;
    background: linear-gradient(160deg, var(--card-black) 0%, var(--card-black-deep) 100%);
    border-bottom: 7px solid var(--gold);
    box-shadow: 0 10px 24px rgba(0,0,0,0.35);
  }
  .company-name {
    position: absolute;
    top: 50%;
    transform: translateY(-50%);
    text-align: center;
    font-weight: 600;
    white-space: nowrap;
  }
  .card-back .company-name {
    left: 0;
    right: 0;
    font-size: 48px;
    color: var(--emboss-tone);
  }
  .card-front .company-name {
    left: 40px;
    width: 390px;
    font-size: 32px;
    color: var(--gold);
  }
  .divider {
    position: absolute;
    left: 448px;
    top: 118px;
    width: 2px;
    height: 250px;
    background: var(--gold);
  }
  .contact-block {
    position: absolute;
    left: 482px;
    top: 112px;
    color: var(--ink-white);
  }
  .person-name {
    font-size: 30px;
    font-weight: 700;
    color: var(--gold);
    letter-spacing: 1px;
    line-height: 1.1;
  }
  .person-title { font-size: 19px; margin-top: 2px; }
  .address { font-size: 20px; line-height: 1.45; margin-top: 22px; }
  .contact-list { list-style: none; margin-top: 18px; font-size: 21px; line-height: 1.4; }
  .contact-list li { display: flex; align-items: center; gap: 8px; }
  .contact-list svg { width: 16px; height: 16px; fill: var(--gold); flex: none; }
</style>
</head>
<body>
<main class="stage">
  <section class="card card-back" aria-label="Card back">
    <p class="company-name">Ironvale Holdings</p>
  </section>

  <section class="card card-front" aria-label="Card front">
    <p class="company-name">Ironvale Holdings</p>
    <div class="divider"></div>
    <div class="contact-block">
      <p class="person-name">DANIEL VERHOEK</p>
      <p class="person-title">Director</p>
      <p class="address">Chemin des Tilleuls 14,<br>Montreux, Vaud 1820, CH</p>
      <ul class="contact-list">
        <li>
          <svg viewBox="0 0 16 16" aria-hidden="true"><path d="M3.5 1l2.5 3-1.5 1.5c.8 2 2.5 3.7 4.5 4.5L10.5 8.5l3 2.5-1.5 3C6 14 2 10 2 2.5z"/></svg>
          021 555 0148
        </li>
        <li>
          <svg viewBox="0 0 16 16" aria-hidden="true"><path d="M1 3h14v10H1z M1 3l7 6 7-6" stroke="#2a2a2c" stroke-width="1.2"/></svg>
          info@ironvaleholdings.com
        </li>
        <li>
          <svg viewBox="0 0 16 16" aria-hidden="true"><circle cx="8" cy="8" r="7"/><path d="M1 8h14M8 1c3 3 3 11 0 14M8 1c-3 3-3 11 0 14" stroke="#2a2a2c" stroke-width="1" fill="none"/></svg>
          www.ironvaleholdings.com
        </li>
      </ul>
    </div>
  </section>
</main>
</body>
</html>
```